We are an integrated facilities management company.

We aggregate everything related to facilities maintenance. Repair-replacement of equipment and facility space materials from:
Asset gathering and tracking.
Vendor screening, contracting and management.
Service requirement development.
Work order processing and management.
Invoice reconciliation.
Vendor payment.
Reporting.
Capital equipment bids and project management.

Target Market(s)

Retail, hospitality, multi-family housing, long term healthcare.

Industry/Entity Type

Maintenance

Contact Information for Business Card

Professional and bold look. (see logo zip file)

Colors
3377b5
85abd2
cedeed

Requirements
Must have
• N/A
Nice to have
• N/A
Should not have
• N/A

```html
<!DOCTYPE html>
<html lang="en">
<head>
<meta charset="utf-8">
<title>Keystone Facility Partners – Business Card</title>
<link rel="stylesheet" href="https://fonts.googleapis.com/css2?family=Arimo:ital,wght@0,400;0,700;1,400&display=swap">
<style>
  :root {
    --blue: #3377b5;
    --blue-light: #85abd2;
    --blue-pale: #cedeed;
    --blue-strip: #3a8cc6;
    --charcoal: #1d2126;
    --charcoal-deep: #121518;
    --black: #050607;
    --silver: #c9ced3;
    --white: #ffffff;
    --muted: #8a9097;
    --backdrop: #e7ebef;
  }
  * { box-sizing: border-box; margin: 0; padding: 0; }
  html, body { width: 1200px; height: 780px; overflow: hidden; }
  body {
    background: var(--backdrop);
    font-family: "Arimo", Arial, sans-serif;
    display: flex;
    align-items: center;
    justify-content: center;
    gap: 40px;
  }
  .card {
    position: relative;
    width: 540px;
    height: 309px;
    border-radius: 14px;
    overflow: hidden;
    box-shadow: 0 10px 26px rgba(0,0,0,.25);
    background: linear-gradient(160deg, var(--charcoal), var(--charcoal-deep));
  }
  .silver-rule {
    position: absolute; left: 0; right: 0; height: 4px;
    background: linear-gradient(90deg, #8d949a, var(--silver), #f2f4f6, var(--silver), #8d949a);
  }
  .brand {
    position: absolute;
    display: flex; align-items: center; gap: 14px;
  }
  .brand-square {
    width: 46px; height: 46px; background: var(--blue); flex: none;
  }
  .brand-text { line-height: 1; }
  .brand-name {
    font-weight: 700; font-size: 24px; color: var(--blue-light);
    letter-spacing: .5px; text-transform: uppercase;
  }
  .brand-tagline {
    margin-top: 8px; font-size: 10px; letter-spacing: 4px;
    color: var(--muted); text-transform: uppercase;
  }

  /* Front */
  .front .brand { left: 40px; top: 48px; }
  .front .silver-rule { top: 138px; }
  .front .contact-band {
    position: absolute; left: 0; right: 0; top: 142px; height: 100px;
    background: var(--black);
  }
  .front .smoke {
    position: absolute; right: 0; top: 0; width: 62%; height: 100%;
    background:
      radial-gradient(ellipse 60% 70% at 70% 100%, rgba(190,210,228,.55), transparent 70%),
      radial-gradient(ellipse 50% 60% at 30% 95%, rgba(150,175,200,.35), transparent 70%),
      linear-gradient(180deg, transparent 40%, rgba(120,150,180,.25));
  }
  .front .person {
    position: absolute; left: 40px; top: 30px; text-align: right; width: 150px;
  }
  .person-name {
    color: var(--white); font-weight: 700; font-size: 17px; text-transform: uppercase;
  }
  .person-role { color: var(--blue-light); font-size: 14px; margin-top: 3px; }
  .front .divider {
    position: absolute; left: 205px; top: 24px; width: 1px; height: 52px;
    background: #9aa1a8;
  }
  .contact-list {
    position: absolute; left: 220px; top: 18px; list-style: none;
  }
  .contact-list li {
    display: flex; align-items: center; gap: 8px;
    color: var(--white); font-size: 13px; line-height: 21px;
  }
  .contact-icon {
    width: 14px; height: 14px; border-radius: 3px; background: #d4d8dc;
    display: flex; align-items: center; justify-content: center;
  }
  .front .address-strip {
    position: absolute; left: 0; right: 0; top: 242px; bottom: 0;
    background: linear-gradient(180deg, var(--blue-strip), var(--blue));
    display: flex; align-items: center; justify-content: center;
    color: var(--white); font-size: 15px; letter-spacing: .3px;
  }

  /* Back */
  .back .brand { left: 40px; top: 34px; }
  .back .silver-rule { top: 112px; }
  .back .services-panel {
    position: absolute; left: 0; right: 0; top: 116px; bottom: 0;
    background: linear-gradient(160deg, #3f93cc, var(--blue));
    padding: 18px 30px 0 34px;
  }
  .services-title {
    color: var(--white); font-weight: 700; font-size: 15px; text-transform: uppercase;
    margin-bottom: 10px;
  }
  .services-columns { display: flex; gap: 24px; }
  .service-list { list-style: none; flex: 1; }
  .service-list li {
    position: relative; padding-left: 16px;
    color: var(--white); font-size: 12.5px; line-height: 20px;
  }
  .service-list li::before {
    content: "\2731"; position: absolute; left: 0; top: 0; font-size: 10px;
  }
</style>
</head>
<body>

  <section class="card front" aria-label="Business card front">
    <div class="brand">
      <span class="brand-square"></span>
      <div class="brand-text">
        <div class="brand-name">Keystone Facility Partners</div>
        <div class="brand-tagline">Inspect · Service · Renew</div>
      </div>
    </div>
    <div class="silver-rule"></div>
    <div class="contact-band">
      <div class="smoke" role="img" aria-label="Soft drifting blue-grey smoke rising from the lower edge"></div>
      <div class="person">
        <div class="person-name">Daniel Brooks</div>
        <div class="person-role">President</div>
      </div>
      <div class="divider"></div>
      <ul class="contact-list">
        <li>
          <span class="contact-icon">
            <svg width="10" height="10" viewBox="0 0 10 10"><path d="M2 1l2 2-1 1.2c.6 1.2 1.6 2.2 2.8 2.8L7 6l2 2-1.2 1.2C4.5 9 1 5.5.8 2.2z" fill="#1d2126"/></svg>
          </span>555.014.2290
        </li>
        <li>
          <span class="contact-icon">
            <svg width="10" height="10" viewBox="0 0 10 10"><rect x="1" y="2.5" width="8" height="5.5" fill="none" stroke="#1d2126" stroke-width="1"/><path d="M1 2.5l4 3 4-3" fill="none" stroke="#1d2126" stroke-width="1"/></svg>
          </span>info@keystonefp.com
        </li>
        <li>
          <span class="contact-icon">
            <svg width="10" height="10" viewBox="0 0 10 10"><circle cx="5" cy="5" r="3.8" fill="none" stroke="#1d2126" stroke-width="1"/><path d="M1.2 5h7.6M5 1.2c-2 2.4-2 5.2 0 7.6M5 1.2c2 2.4 2 5.2 0 7.6" fill="none" stroke="#1d2126" stroke-width=".8"/></svg>
          </span>www.keystonefp.com
        </li>
      </ul>
    </div>
    <div class="address-strip">PO BOX 480, Mesa Road, 4th Lane, Arizona 85201</div>
  </section>

  <section class="card back" aria-label="Business card back">
    <div class="brand">
      <span class="brand-square"></span>
      <div class="brand-text">
        <div class="brand-name">Keystone Facility Partners</div>
        <div class="brand-tagline">Inspect · Service · Renew</div>
      </div>
    </div>
    <div class="silver-rule"></div>
    <div class="services-panel">
      <h2 class="services-title">Services</h2>
      <div class="services-columns">
        <ul class="service-list">
          <li>Asset gathering and tracking.</li>
          <li>Vendor screening, contracting and management.</li>
          <li>Service requirement development.</li>
          <li>Work order processing and management.</li>
        </ul>
        <ul class="service-list">
          <li>Invoice reconciliation.</li>
          <li>Vendor payment.</li>
          <li>Reporting.</li>
          <li>Capital equipment bids and project management.</li>
        </ul>
      </div>
    </div>
  </section>

</body>
</html>
```